www.dunmoreplumbingandheating.com

I want everything on this page plus I need to add a ad that say save up to 20% on new installation.. also need to add a TFR logo sense I sing up with the TFR in San Diego CA. Just need this page to look more professional.
I had come to realize that I will need to convert the SPD file to HTML in order to upload to my site, so if any one is interested in doing the complete work let me know I know I need to raise my budget which I am working on that already. I had contacted support.
Remember for the header where you guys use picture, I be using my on pictures most likely a slide show of pictures so one design with different picture don't make different because I still will replaced it with my own. at my location in my industry the customer the faster they can see the phone number, the services and company experience the better.
New customers

```html
<!DOCTYPE html>
<html lang="en">
<head>
<meta charset="utf-8">
<title>Dunmore Plumbing &amp; Heating Inc.</title>
<link rel="stylesheet" href="https://fonts.googleapis.com/css2?family=Open+Sans:ital,wght@0,400;0,600;0,700;1,400;1,600;1,700&family=Roboto+Condensed:wght@700&family=Ubuntu:ital,wght@1,500&display=swap">
<style>
:root{
  --blue:#0a86c9;
  --blue-dark:#0a5f9e;
  --maroon:#7f2424;
  --maroon-dark:#6a1c1c;
  --orange:#f39a12;
  --orange-deep:#ec7f0a;
  --yellow:#f7c31a;
  --text:#333;
  --muted:#555;
  --rule:#d9d9d9;
  --teal:#0e5b77;
  --white:#fff;
}
*{box-sizing:border-box;margin:0;padding:0}
html,body{width:1200px;height:1192px;overflow:hidden}
body{position:relative;background:var(--white);font-family:"Open Sans",Arial,sans-serif;color:var(--text)}
.abs{position:absolute}

.top-bar{left:0;top:0;width:1200px;height:37px;background:linear-gradient(90deg,var(--blue-dark),var(--blue) 50%,var(--blue-dark))}
.social{display:flex;gap:8px}
.social span{display:block;width:23px;height:23px;background:var(--white);border-radius:2px}
.top-bar .social{position:absolute;left:942px;top:7px}

.brand{left:141px;top:36px;display:flex;align-items:center;gap:8px}
.brand-dot{width:22px;height:22px;border-radius:50%;background:var(--orange)}
.brand-name{font-weight:700;font-size:14px;line-height:16px;color:var(--maroon);letter-spacing:.3px}

.contact-line{top:60px;display:flex;align-items:center;gap:10px;font-size:17px;color:#333}
.contact-line svg{display:block}
.header-phone{left:587px}
.header-email{left:751px}
.divider-v{left:735px;top:50px;width:1px;height:46px;background:linear-gradient(#fff,#ccc,#fff)}

.main-nav{left:141px;top:112px;width:918px;height:42px;background:linear-gradient(var(--maroon),var(--maroon-dark));border-radius:3px;display:flex;align-items:center;color:var(--white);font-size:15px;font-weight:600}
.main-nav a{color:inherit;text-decoration:none;height:100%;display:flex;align-items:center;justify-content:center;border-right:1px solid rgba(255,255,255,.25)}
.main-nav a.active{background:linear-gradient(var(--yellow),var(--orange-deep));border-radius:3px 0 0 3px}
.nav-home{width:110px}.nav-about{width:142px}.nav-services{width:132px}.nav-contact{width:159px}
.emergency{margin-left:auto;margin-right:22px;font-style:italic;font-weight:700;font-size:16px}
.emergency b{color:var(--yellow)}

.hero{left:141px;top:160px;width:918px;height:346px;background:linear-gradient(100deg,#cbb9a4 0%,#e3d8cb 35%,#b9b7b5 60%,#d8cfc4 100%)}
.hero-caption{left:572px;top:419px;width:487px;height:31px;background:rgba(20,20,20,.85);color:var(--white);font-family:"Roboto Condensed",Arial,sans-serif;font-size:19px;line-height:31px;padding-left:15px}
.hero-dots{left:966px;top:481px;display:flex;gap:7px}
.hero-dots i{width:14px;height:4px;background:var(--blue)}
.hero-dots i.on{background:var(--maroon)}

.card{top:535px;width:290px;height:263px;background:var(--white);border:1px solid #ddd;border-radius:4px;overflow:hidden;box-shadow:0 8px 6px -6px rgba(0,0,0,.35)}
.card-about{left:141px}.card-services{left:455px}.card-contact{left:769px}
.card-head{height:40px;background:var(--maroon);color:var(--white);font-size:21px;font-weight:600;line-height:42px;padding-left:66px}
.card-corner{position:absolute;right:0;bottom:0;width:46px;height:46px;background:linear-gradient(135deg,transparent 50%,var(--blue) 50%)}
.card-corner::before,.card-corner::after{content:"";position:absolute;background:var(--white)}
.card-corner::before{right:10px;bottom:18px;width:14px;height:2px}
.card-corner::after{right:16px;bottom:12px;width:2px;height:14px}
.about-body{padding:10px 15px;font-size:12px;line-height:18px;color:var(--muted);letter-spacing:.3px}
.about-lead{font-weight:600;color:#222;margin-bottom:10px;text-align:justify}
.service-list{list-style:none;padding:6px 21px 0 20px}
.service-list li{height:34px;display:flex;align-items:center;gap:12px;font-size:13px;font-weight:600;color:#333;border-bottom:1px dotted var(--rule)}
.service-list li:last-child{border-bottom:0}
.quick-form{padding:12px 19px 0 19px;display:flex;flex-direction:column;gap:10px}
.field{height:29px;border:1px solid #ccc;border-radius:2px;display:flex;align-items:center;gap:10px;padding-left:8px;font-style:italic;font-size:13px;color:#555}
.field-message{height:61px;align-items:flex-start;padding-top:7px}

.promo{left:141px;top:887px;width:604px;height:35px;background:var(--maroon);border-radius:4px;color:var(--white);font-family:"Ubuntu",Arial,sans-serif;font-style:italic;font-weight:500;font-size:26px;line-height:35px;padding-left:12px}
.promo b{color:var(--yellow);font-weight:500}
.accredit-badge{left:769px;top:841px;width:290px;height:110px;border:2px solid var(--teal);border-radius:12px;overflow:hidden;background:var(--teal)}
.accredit-badge::before{content:"";position:absolute;left:0;top:0;width:98px;height:100%;background:var(--white)}

.site-footer{left:0;top:979px;width:1200px;height:180px;background:linear-gradient(var(--orange-deep),var(--orange))}
.foot-col{top:17px;color:var(--white)}
.foot-col h3{font-size:14px;font-weight:700;letter-spacing:.5px;padding-bottom:4px;border-bottom:1px solid rgba(255,255,255,.45);margin-bottom:8px}
.col-links{left:142px;width:125px}
.col-contact{left:331px;width:240px}
.col-map{left:638px;width:223px}
.link-list{list-style:none;font-size:13px}
.link-list li{height:27px;display:flex;align-items:center;gap:9px}
.link-list li::before{content:"›";font-size:14px}
.info-row{display:flex;gap:14px;font-size:13px;line-height:17px;margin-bottom:15px}
.info-row svg{flex:none;margin-top:2px}
.map{width:222px;height:92px;background:linear-gradient(120deg,#e6e2dc,#d7d3cc)}
.map-link{font-size:12px;margin-top:7px;padding-left:3px}
.foot-brand{left:925px;top:1072px;font-weight:700;font-size:14px;line-height:16px;color:rgba(255,255,255,.6);letter-spacing:.3px}

.bottom-bar{left:0;top:1159px;width:1200px;height:33px;background:var(--maroon);color:var(--white);font-size:13px;line-height:33px}
.bottom-bar .copy{position:absolute;left:141px}
.bottom-bar .social{position:absolute;left:939px;top:5px}
</style>
</head>
<body>

<div class="abs top-bar">
  <div class="social" aria-label="Social links"><span></span><span></span><span></span><span></span></div>
</div>

<div class="abs brand">
  <span class="brand-dot"></span>
  <span class="brand-name">DUNMORE PLUMBING<br>&amp; HEATING INC.</span>
</div>

<div class="abs contact-line header-phone">
  <svg width="18" height="18" viewBox="0 0 24 24"><path fill="#7f2424" d="M6.6 10.8a15 15 0 0 0 6.6 6.6l2.2-2.2c.3-.3.7-.4 1-.2 1.1.4 2.3.6 3.6.6.6 0 1 .4 1 1V20c0 .6-.4 1-1 1A17 17 0 0 1 3 4c0-.6.4-1 1-1h3.5c.6 0 1 .4 1 1 0 1.3.2 2.5.6 3.6.1.3 0 .7-.2 1z"/></svg>
  1-760-555-0142
</div>
<div class="abs divider-v"></div>
<div class="abs contact-line header-email">
  <svg width="22" height="15" viewBox="0 0 22 15"><rect width="22" height="15" fill="#7f2424"/><path d="M1 1l10 8 10-8" stroke="#fff" stroke-width="1.6" fill="none"/></svg>
  info@dunmoreplumbingandheating.com
</div>

<nav class="abs main-nav">
  <a class="nav-home active" href="#">HOME</a>
  <a class="nav-about" href="#">ABOUT US</a>
  <a class="nav-services" href="#">SERVICES</a>
  <a class="nav-contact" href="#">CONTACT US</a>
  <span class="emergency">24 Hour Emergency Service : <b>760 555-0187</b></span>
</nav>

<div class="abs hero" role="img" aria-label="Photo of a hand tightening a chrome sink pipe with a red pipe wrench against tiled wall"></div>
<div class="abs hero-caption">PROVIDING QUALITY WORK AT AFFORDABLE PRICES</div>
<div class="abs hero-dots"><i></i><i class="on"></i><i></i><i></i></div>

<section class="abs card card-about">
  <div class="card-head">ABOUT US</div>
  <div class="about-body">
    <p class="about-lead">Ut wisi nim ad minim veniam, quis sit exetiper suscipit lobortis nisl ut aliquip ex ea comm Duis autem vel eum iriure.</p>
    <p>Lorem ipsum dolor sit amet, consectetuer adipiscing elit, sed diam nonummy nibh euismod tincidunt ut laoreet dolore magna aliquam erat volutpat. Ut wisi enim ad minim veniam, quis nostrud exerci tation ullamcorper suscipit lobortis nisl ut aliquip ex ea commodo consequat</p>
  </div>
  <span class="card-corner"></span>
</section>

<section class="abs card card-services">
  <div class="card-head">OUR SERVICES</div>
  <ul class="service-list">
    <li><svg width="8" height="12" viewBox="0 0 8 12"><path d="M1 1l5 5-5 5" stroke="#ec7f0a" stroke-width="2.2" fill="none"/></svg>Water Heater Repair &amp; Installation</li>
    <li><svg width="8" height="12" viewBox="0 0 8 12"><path d="M1 1l5 5-5 5" stroke="#ec7f0a" stroke-width="2.2" fill="none"/></svg>Boiler Repair &amp; Installation</li>
    <li><svg width="8" height="12" viewBox="0 0 8 12"><path d="M1 1l5 5-5 5" stroke="#ec7f0a" stroke-width="2.2" fill="none"/></svg>Bathroom renovation</li>
    <li><svg width="8" height="12" viewBox="0 0 8 12"><path d="M1 1l5 5-5 5" stroke="#ec7f0a" stroke-width="2.2" fill="none"/></svg>Kitchen Renovation</li>
    <li><svg width="8" height="12" viewBox="0 0 8 12"><path d="M1 1l5 5-5 5" stroke="#ec7f0a" stroke-width="2.2" fill="none"/></svg>Water meters</li>
    <li><svg width="8" height="12" viewBox="0 0 8 12"><path d="M1 1l5 5-5 5" stroke="#ec7f0a" stroke-width="2.2" fill="none"/></svg>Gas Meters</li>
  </ul>
  <span class="card-corner"></span>
</section>

<section class="abs card card-contact">
  <div class="card-head">QUICK CONTACT</div>
  <div class="quick-form">
    <div class="field"><svg width="12" height="13" viewBox="0 0 12 13"><circle cx="6" cy="3.5" r="3.2" fill="#7f2424"/><path d="M0 13c0-4 2.5-5.5 6-5.5s6 1.5 6 5.5z" fill="#7f2424"/></svg>Name</div>
    <div class="field"><svg width="14" height="10" viewBox="0 0 14 10"><rect width="14" height="10" fill="#7f2424"/><path d="M1 1l6 5 6-5" stroke="#fff" stroke-width="1.2" fill="none"/></svg>Email</div>
    <div class="field"><svg width="13" height="13" viewBox="0 0 24 24"><path fill="#7f2424" d="M6.6 10.8a15 15 0 0 0 6.6 6.6l2.2-2.2c.3-.3.7-.4 1-.2 1.1.4 2.3.6 3.6.6.6 0 1 .4 1 1V20c0 .6-.4 1-1 1A17 17 0 0 1 3 4c0-.6.4-1 1-1h3.5c.6 0 1 .4 1 1 0 1.3.2 2.5.6 3.6.1.3 0 .7-.2 1z"/></svg>Phone</div>
    <div class="field field-message"><svg width="13" height="13" viewBox="0 0 13 13"><rect x="1" y="2" width="9" height="10" fill="none" stroke="#7f2424" stroke-width="1.5"/><path d="M5 8l7-7" stroke="#7f2424" stroke-width="2"/></svg>Message</div>
  </div>
  <span class="card-corner"></span>
</section>

<div class="abs promo">Save Up To <b>20%</b> On New Installation..</div>
<div class="abs accredit-badge" role="img" aria-label="TFR accredited business badge"></div>

<footer class="abs site-footer">
  <div class="abs foot-col col-links">
    <h3>QUICK LINKS</h3>
    <ul class="link-list"><li>Home</li><li>About Us</li><li>Services</li><li>Contact Us</li></ul>
  </div>
  <div class="abs foot-col col-contact">
    <h3>CONTACT DETAILS</h3>
    <div class="info-row"><svg width="11" height="14" viewBox="0 0 11 14"><path d="M5.5 0A5.5 5.5 0 0 0 0 5.5C0 9.5 5.5 14 5.5 14S11 9.5 11 5.5A5.5 5.5 0 0 0 5.5 0zm0 7.5a2 2 0 1 1 0-4 2 2 0 0 1 0 4z" fill="#7f2424"/></svg><span>Lorem ipsum dolor sit consectetue<br>Street No 5, zip Code: 897410</span></div>
    <div class="info-row"><svg width="13" height="13" viewBox="0 0 24 24"><path fill="#7f2424" d="M6.6 10.8a15 15 0 0 0 6.6 6.6l2.2-2.2c.3-.3.7-.4 1-.2 1.1.4 2.3.6 3.6.6.6 0 1 .4 1 1V20c0 .6-.4 1-1 1A17 17 0 0 1 3 4c0-.6.4-1 1-1h3.5c.6 0 1 .4 1 1 0 1.3.2 2.5.6 3.6.1.3 0 .7-.2 1z"/></svg><span>1-760-555-0142</span></div>
    <div class="info-row"><svg width="13" height="10" viewBox="0 0 14 10"><rect width="14" height="10" fill="#7f2424"/><path d="M1 1l6 5 6-5" stroke="#f39a12" stroke-width="1.2" fill="none"/></svg><span>info@dunmoreplumbingandheating.com</span></div>
  </div>
  <div class="abs foot-col col-map">
    <h3>LOCATION MAP</h3>
    <div class="map" role="img" aria-label="Street map showing the business location"></div>
    <div class="map-link">View Location »</div>
  </div>
</footer>
<div class="abs foot-brand">DUNMORE PLUMBING<br>&amp; HEATING INC.</div>

<div class="abs bottom-bar">
  <span class="copy">© 2014 DUNMORE PLUMBING &amp; HEATING INC.ALL RIGHTS RESERVED.</span>
  <div class="social" aria-label="Social links"><span></span><span></span><span></span><span></span></div>
</div>

</body>
</html>
```